Business Card Design Project

Brightfern Consulting is a newly created boutique consultancy focussing on delivering strategic consulting to medium and large businesses, with a focus on:
- Strategic planning and execution.
- Corporate function optimisation, especially in the areas of finance, commercial, and IT. This includes implementing the right functional design for the needs of the business, and ensuring the right skills.
- Performance management, in particular project governance and control, operational metrics and management reporting.
I have in mind a tag line for the business being:
"Helping business to discover sustainable value."
I am looking for a letterhead design which utilises my new logo on report templates (powerpoint and word), and letterhead.
Trivopedix defines a mother lode as follows:
"Mother lode is a principal vein or zone of veins of gold or silver ore. The term probably came from a literal translation of the Spanish veta madre, a term common in old Mexican mining. Veta madre, for instance, is the name given to an 11-kilometre-long (6.8 mi) silver vein discovered in 1548 in Guanajuato, New Spain (modern-day Mexico)."
My preference is for black and gold. Logo files are attached in .eps format. All fonts are outlined. The fonts that are used are "Crimson Text" and "Josefin Sans". They are free open source fonts and they are available here: http://www.typevault.example/fonts
Target Market(s)
Medium to large corporates.
Industry/Entity Type
Boutique
Font styles to use
Other font styles liked:
- All Fonts Are Outlined. The Fonts That Are Used Are "Crimson Text" And "Josefin Sans". They Are Free Open Source Fonts And They Are Available Here: Http://www.typevault.example/fonts
Look and feel
Each slider illustrates characteristics of the customer's brand and the style your logo design should communicate.

```html
<!DOCTYPE html>
<html lang="en">
<head>
<meta charset="utf-8">
<title>Brightfern Consulting – Business Cards</title>
<link rel="stylesheet" href="https://fonts.googleapis.com/css2?family=Crimson+Text:wght@400;600&family=Josefin+Sans:wght@400;600&family=Arimo:wght@400&display=swap">
<style>
  :root {
    --backdrop: #e9e6e1;
    --card-black: #0d0d0e;
    --card-black-edge: #202124;
    --card-white: #ffffff;
    --gold: #c9962c;
    --gold-soft: #d4a640;
    --ink: #111111;
    --silver: #d9d9d9;
    --grey-text: #3a3a3a;
  }
  * { box-sizing: border-box; margin: 0; padding: 0; }
  html, body {
    width: 1200px;
    height: 784px;
    overflow: hidden;
    background: var(--backdrop);
  }
  .canvas {
    position: relative;
    width: 1200px;
    height: 784px;
    display: flex;
    align-items: center;
    justify-content: center;
    gap: 40px;
  }
  .card {
    position: relative;
    width: 560px;
    height: 320px;
    overflow: hidden;
    box-shadow: 0 6px 18px rgba(0,0,0,0.18);
  }

  /* Front (black) */
  .card--front {
    background: radial-gradient(ellipse at 50% 35%, var(--card-black-edge) 0%, var(--card-black) 70%);
    display: flex;
    flex-direction: column;
    align-items: center;
    justify-content: center;
  }
  .front-mark {
    width: 74px;
    height: 74px;
    border: 7px solid var(--silver);
    margin-bottom: 22px;
  }
  .front-name {
    font-family: "Crimson Text", serif;
    font-weight: 400;
    font-size: 40px;
    letter-spacing: 2px;
    text-transform: uppercase;
    color: var(--silver);
    line-height: 1;
  }
  .front-tagline {
    margin-top: 14px;
    font-family: "Josefin Sans", sans-serif;
    font-size: 10px;
    letter-spacing: 1.6px;
    text-transform: uppercase;
    color: var(--silver);
  }

  /* Back (white) */
  .card--back { background: var(--card-white); }
  .holder {
    position: absolute;
    top: 22px;
    right: 28px;
    text-align: right;
    font-family: "Arimo", sans-serif;
  }
  .holder-name { color: var(--gold); font-size: 15px; }
  .holder-role { color: var(--ink); font-size: 11px; margin-top: 2px; }

  .brand-row {
    position: absolute;
    left: 30px;
    top: 78px;
    display: flex;
    align-items: center;
    gap: 16px;
  }
  .brand-mark {
    width: 78px;
    height: 78px;
    border: 8px solid var(--ink);
  }
  .brand-name {
    font-family: "Crimson Text", serif;
    font-weight: 400;
    font-size: 30px;
    letter-spacing: 1px;
    text-transform: uppercase;
    color: var(--ink);
    line-height: 1;
  }
  .tagline-band {
    position: absolute;
    left: 0;
    right: 0;
    top: 172px;
    height: 22px;
    background: var(--ink);
    display: flex;
    align-items: center;
    padding-left: 30px;
  }
  .tagline {
    font-family: "Josefin Sans", sans-serif;
    font-size: 14px;
    letter-spacing: 1px;
    color: var(--gold-soft);
    line-height: 1;
    padding-top: 2px;
  }
  .contact-list {
    position: absolute;
    left: 30px;
    top: 206px;
    list-style: none;
    font-family: "Arimo", sans-serif;
    font-size: 17px;
    color: var(--grey-text);
  }
  .contact-item {
    display: flex;
    align-items: center;
    gap: 7px;
    height: 21px;
  }
  .contact-item--indent { padding-left: 25px; }
  .contact-icon { width: 18px; height: 18px; flex: none; }
  .contact-icon path, .contact-icon circle, .contact-icon rect { fill: var(--gold); }
  .contact-icon .stroke { fill: none; stroke: var(--gold); stroke-width: 1.6; }
</style>
</head>
<body>
<main class="canvas">

  <section class="card card--front" aria-label="Business card front">
    <div class="front-mark"></div>
    <p class="front-name">Brightfern Consulting</p>
    <p class="front-tagline">Helping business discover sustainable value</p>
  </section>

  <section class="card card--back" aria-label="Business card back">
    <div class="holder">
      <p class="holder-name">Dana Whitlow</p>
      <p class="holder-role">Manager</p>
    </div>

    <div class="brand-row">
      <div class="brand-mark"></div>
      <p class="brand-name">Brightfern Consulting</p>
    </div>

    <div class="tagline-band">
      <p class="tagline">Helping business to discover sustainable value</p>
    </div>

    <ul class="contact-list">
      <li class="contact-item">
        <svg class="contact-icon" viewBox="0 0 20 20" aria-hidden="true">
          <path d="M5 2l3 4-2 2c1 2.5 3.5 5 6 6l2-2 4 3-2 3C9 18 2 11 2 4z"/>
        </svg>
        <span>(08) 9000 4127</span>
      </li>
      <li class="contact-item">
        <svg class="contact-icon" viewBox="0 0 20 20" aria-hidden="true">
          <circle class="stroke" cx="10" cy="10" r="8"/>
          <path class="stroke" d="M2 10h16M10 2c-4 4-4 12 0 16M10 2c4 4 4 12 0 16"/>
        </svg>
        <span>www.brightfern.example</span>
      </li>
      <li class="contact-item">
        <svg class="contact-icon" viewBox="0 0 20 20" aria-hidden="true">
          <rect class="stroke" x="2" y="5" width="16" height="11"/>
          <path class="stroke" d="M2 5l8 6 8-6"/>
        </svg>
        <span>hello@brightfern.example</span>
      </li>
      <li class="contact-item">
        <svg class="contact-icon" viewBox="0 0 20 20" aria-hidden="true">
          <path d="M10 2L1 10h3v8h5v-5h2v5h5v-8h3z"/>
        </svg>
        <span>PO Box 418 mill lane street</span>
      </li>
      <li class="contact-item contact-item--indent">
        <span>Kelmora, Western Australia, 6999</span>
      </li>
    </ul>
  </section>

</main>
</body>
</html>
```